Lender's Roundup - Edison NJ 2010

We need an event program designed for our Lender's Roundup events. We will have ten events in 2010 so we need a boiler plate layout for them all, however the thing that will change for each city are the speakers pictures, bios, logos and our ad sponsors. The program will include a cover page and on the backside of the cover page a Welcome page with a message from our founder. The next page (facing the inside front cover page) will be About the Lender's Roundup message. The next few pages will be reserved for our featured speakers and they will each have their own page to include their picture, company logo and bio. the remaining pages will be for our sponsors, which will vary by city/location. The back page should include the logos of all our sponsors, by category. I would like the brochure to be small in size...roughly 6 5/8" by 6 7/8". These are CEO events so the program needs to be professional, sophisticated, with an edge. Look at our website for more information about our next event on July 21st. I've included one of our speakers pictures, bio and company logo for setup purposes.

Target Market(s)

The attendees of our events are CEOs and Chief Decision Makers.

Industry/Entity Type

Events

Requirements
Must have
• The program must use all the photos, bios and logos we've attached.
Nice to have
• I like modern, clean lines, with a slight edge.
Should not have
• This should not be a consumer designed piece. It needs to have the WOW factor of professionalism.

```html
<!DOCTYPE html>
<html lang="en">
<head>
<meta charset="utf-8">
<title>Lender's Roundup – Event Program</title>
<link rel="stylesheet" href="https://fonts.googleapis.com/css2?family=Source+Sans+3:wght@400;600;700&display=swap">
<style>
  :root {
    --backdrop: #cbcbcb;
    --signal-red: #d42a26;
    --ink-grey: #5a5a5c;
    --page-dark: #59595b;
    --paper: #ffffff;
    --body-ink: #3c3c3e;
    --rule: #8c8c8e;
    --bank-blue: #27408b;
    --bank-maroon: #7a1f36;
  }
  * { box-sizing: border-box; margin: 0; padding: 0; }
  html, body { width: 1200px; height: 900px; overflow: hidden; }
  body {
    position: relative;
    background: var(--backdrop);
    font-family: "Source Sans 3", "Helvetica Neue", Arial, sans-serif;
  }

  /* ---------- Covers ---------- */
  .cover {
    position: absolute;
    top: 35px;
    width: 282px;
    height: 292px;
    box-shadow: 3px 4px 6px rgba(0,0,0,.35);
    overflow: hidden;
  }
  .cover--suit { left: 119px; width: 263px; background: linear-gradient(135deg, #6e5a49 0%, #4a3a2e 45%, #2e241c 100%); }
  .cover--note { left: 459px; background: radial-gradient(ellipse at 45% 35%, #e6e6e4 0%, #bdbdbb 55%, #8f8f8d 100%); }
  .cover--tower { left: 800px; width: 280px; background: linear-gradient(120deg, #9a9a9a 0%, #c8c8c8 40%, #6e6e6e 70%, #9c9c9c 100%); }
  .cover__art { position: absolute; inset: 0; }
  .cover__tag {
    position: absolute;
    top: 18px; left: 0;
    width: 71px; height: 27px;
    background: var(--signal-red);
  }
  .cover__label {
    position: absolute;
    top: 13px; left: 71px; right: 8px;
    height: 35px;
    background: var(--paper);
    padding: 3px 0 0 7px;
    font-size: 7.4px;
    line-height: 8.4px;
    font-weight: 600;
    color: var(--ink-grey);
  }
  .cover__label .event-name { color: var(--signal-red); }
  .cover__brand {
    position: absolute;
    left: 16px; bottom: 20px;
    font-size: 12px;
    font-weight: 600;
    letter-spacing: -.2px;
    color: var(--paper);
  }
  .cover--note .cover__brand { color: #4a4a4c; }

  /* ---------- Spread ---------- */
  .spread {
    position: absolute;
    left: 118px; top: 366px;
    width: 964px; height: 494px;
    box-shadow: 3px 4px 7px rgba(0,0,0,.35);
  }
  .page {
    position: absolute;
    top: 0; height: 100%;
    overflow: hidden;
  }
  .page--dark { left: 0; width: 482px; background: var(--page-dark); color: var(--paper); }
  .page--light { left: 482px; width: 482px; background: var(--paper); color: var(--body-ink); }

  .speaker-head__tag {
    position: absolute;
    top: 23px; left: 0;
    width: 127px; height: 49px;
    background: var(--signal-red);
  }
  .page--light .speaker-head__tag { width: 122px; }
  .speaker-head__box {
    position: absolute;
    top: 23px; left: 127px; right: 2px;
    height: 49px;
    background: var(--paper);
    border: 1px solid var(--rule);
    padding: 10px 0 0 12px;
    font-size: 12.5px;
    line-height: 14px;
    font-weight: 700;
    color: var(--ink-grey);
  }
  .page--light .speaker-head__box { left: 122px; padding-left: 16px; }
  .speaker-head__name { color: var(--signal-red); }

  .speaker-photo {
    position: absolute;
    top: 97px; left: 22px;
    width: 98px; height: 114px;
  }
  .page--dark .speaker-photo { background: linear-gradient(160deg, #8a6a4e 0%, #4b3a2c 55%, #22242a 100%); }
  .page--light .speaker-photo { background: linear-gradient(160deg, #6f5a45 0%, #b89478 50%, #3e3a3a 100%); }

  .contact {
    position: absolute;
    top: 217px; left: 22px;
    width: 112px;
    font-size: 7.6px;
    line-height: 9.2px;
  }
  .contact dt { margin-top: 1.8px; }
  .contact dd { overflow-wrap: anywhere; }
  .page--light .contact { color: var(--signal-red); }

  .bio {
    position: absolute;
    top: 97px;
    height: 372px;
    font-size: 7.55px;
    line-height: 9.1px;
    column-count: 2;
    column-fill: auto;
  }
  .bio p + p { text-indent: 10px; }
  .bio .bio__col-start { break-before: column; text-indent: 10px; }
  .page--dark .bio { left: 136px; width: 320px; column-gap: 22px; }
  .page--light .bio { left: 132px; width: 340px; column-gap: 12px; }

  .company-mark {
    position: absolute;
    top: 427px; left: 22px;
    display: flex; align-items: center; gap: 5px;
    font-size: 9.5px; line-height: 10px;
    font-weight: 600;
  }
  .company-mark__square { width: 10px; height: 10px; flex: none; }
  .page--dark .company-mark {
    width: 98px; height: 40px;
    background: var(--paper);
    padding: 0 6px;
    color: var(--bank-blue);
  }
  .page--dark .company-mark__square { background: var(--bank-blue); }
  .page--light .company-mark {
    width: 90px; height: 38px;
    color: var(--bank-maroon);
  }
  .page--light .company-mark__square { background: var(--bank-maroon); }
</style>
</head>
<body>

  <!-- Cover variants -->
  <section class="cover cover--suit">
    <div class="cover__art" role="img" aria-label="Close-up photograph of a brown pinstripe suit fabric"></div>
    <div class="cover__tag"></div>
    <div class="cover__label">
      <span class="event-name">North Jersey Lender's Roundup™</span><br>
      Linden Hall, Edison NJ, November 9, 2010,<br>
      CEO Signature Event.
    </div>
    <div class="cover__brand">Lender'sRoundup.</div>
  </section>

  <section class="cover cover--note">
    <div class="cover__art" role="img" aria-label="Engraved banknote portrait detail in grey tones"></div>
    <div class="cover__tag"></div>
    <div class="cover__label">
      <span class="event-name">North Jersey Lender's Roundup™</span><br>
      Linden Hall, Edison NJ, November 9, 2010,<br>
      CEO Signature Event.
    </div>
    <div class="cover__brand">Lender'sRoundup.</div>
  </section>

  <section class="cover cover--tower">
    <div class="cover__art" role="img" aria-label="Upward view of a glass office tower in grey tones"></div>
    <div class="cover__tag"></div>
    <div class="cover__label">
      <span class="event-name">North Jersey Lender's Roundup™</span><br>
      Linden Hall, Edison NJ, November 9, 2010,<br>
      CEO Signature Event.
    </div>
    <div class="cover__brand">Lender'sRoundup.</div>
  </section>

  <!-- Speaker spread -->
  <section class="spread">

    <article class="page page--dark">
      <div class="speaker-head__tag"></div>
      <header class="speaker-head__box">
        <div class="speaker-head__name">Marcus Delvecchio III</div>
        <div>President &amp; CEO of Ridgeline Valley Community Bank</div>
      </header>
      <div class="speaker-photo" role="img" aria-label="Portrait photograph of speaker Marcus Delvecchio III"></div>
      <dl class="contact">
        <dt>Email</dt><dd>mdelvecchio@pccb.example</dd>
        <dt>Web</dt><dd>www.pccb.example</dd>
        <dt>Chirp</dt><dd>@MarcusD3</dd>
        <dt>Profile</dt><dd>Marcus.Delvecchio3</dd>
        <dt>Network</dt><dd>www.netlink.example/in/<br>marcusdelvecchio</dd>
        <dt>Blog</dt><dd>www.lendingonmainst.example</dd>
        <dt>Phone</dt><dd>201-555-0142</dd>
      </dl>
      <div class="bio">
        <p>Marcus Delvecchio III is Chairman and CEO of Palisade Crest Community Bank (PCCB), the fastest growing bank in New Jersey history with seven branches in Englewood Cliffs, Fort Lee, Cresskill, Hackensack, West New York and Ridgewood. The bank was founded by Mr. Delvecchio and other Bergen County civic and business leaders to serve local residents and businesses by providing the highest level of personalized community banking services to Northern New Jersey.</p>
        <p>As Chairman and CEO of Palisade Crest Community Bank, Mr. Delvecchio is responsible for the bank's business development plan, serves as the bank's liaison to the community, sits on the bank's loan committee and serves as the bank's spokesperson. Mr. Delvecchio has been instrumental in developing the bank's branch and expansion strategy and oversees all marketing activities.</p>
        <p>PCCB's board of directors, shareholders, employees and loyal customer base have all contributed to its unprecedented growth. Since opening its first branch in January 2005, PCCB has grown to more than $500 million in assets.</p>
        <p class="bio__col-start">Palisade Crest Community Bank was recently named in the Top 10 on NJ Business Weekly's 50 Fastest Growing Companies list and was a finalist for the publication's Emerging Business of the Year award.</p>
        <p>In addition, PCCB was also a recipient of the Enterprise Excellence Awards–the most esteemed and sought after small-business awards in the United States. The Enterprise Excellence Awards honor the visionary practices and exemplary achievements of a select few small businesses.</p>
        <p>Mr. Delvecchio is a frequent commentator on BizNet TV, Market Wire Radio and Capital Street News discussing Community Banking issues.</p>
        <p>Previously, Mr. Delvecchio was president of MDC Construction, Inc. a family owned third generation construction business that was founded in 1979. MDC is a building, construction management and development firm based in Englewood Cliffs, New Jersey that specializes in custom built luxury residential homes specially built for clients as well as for general sale.</p>
        <p>Mr. Delvecchio received his bachelor's degree in science in Construction Engineering Technology from Northfield University in 1987. He was named "Builder of the Year" in 1995 by the Builders Guild of Northern New Jersey and was also awarded the Founders Medal from Bergen Prep High School in 2005.</p>
      </div>
      <div class="company-mark"><span class="company-mark__square"></span><span>Palisade Crest Community Bank</span></div>
    </article>

    <article class="page page--light">
      <div class="speaker-head__tag"></div>
      <header class="speaker-head__box">
        <div class="speaker-head__name">Gerald Haskins</div>
        <div>President &amp; CEO of Ridgeline Valley Community Bank</div>
      </header>
      <div class="speaker-photo" role="img" aria-label="Portrait photograph of speaker Gerald Haskins"></div>
      <dl class="contact">
        <dt>Email</dt><dd>mdelvecchio@pccb.example</dd>
        <dt>Web</dt><dd>www.pccb.example</dd>
        <dt>Chirp</dt><dd>@MarcusD3</dd>
        <dt>Profile</dt><dd>Marcus.Delvecchio3</dd>
        <dt>Network</dt><dd>www.netlink.example/in/<br>marcusdelvecchio</dd>
        <dt>Blog</dt><dd>www.lendingonmainst.example</dd>
        <dt>Phone</dt><dd>201-555-0142</dd>
      </dl>
      <div class="bio">
        <p>Wis esting et, con henim velis er si et lor sisisequatis eum il doloreet exerit utpat. Ut am ad tio dolenit praessim dui ex ero dolobore feu feuipit lut la feum accumsandre molore commy niam, senibh el dolore feuguer ing eu feuis adionsequis amconse quipiss endigna facipit eraesecte delit wisciduisis nulput lortie enibh ex enibh ero dionsequat acil dolorpero deliquam quipisl diam, conum zzrit ilit volore feugait nulputat nostinis dunt numsan ea feumsandio er sit aliquam aliquis augiat vel delesse quatet nullamet autpat wisi.</p>
        <p>Endio odoloreet autpat nulputatum inibh esed minim quisit praessequis nullaor eraessenim nis dunt ate dipit la cortis dolorem iusci ex et nibh ea facidunt augiat alit inim nos nulla faci blaor sequis atio consent augue magna consequ amconsecte tincidunt vulla feugiat nim ilisisit la aci blandreros nim nullaor perostie deliquat. Duisci tie del eumsan ulputem quatie dolorper atum ilit, coreet, sim nos nonulla con hendiam am del ulla feugiam er auguero esed et augait lam, consecte con vero odo et ing eugait ad tat. Duiscill inibh exer si blaore dui blam incil dio od modoloboreet et, veliqui elent diatuerci tio odolore min henibh eniamet am, sequamc onulla alismod ionsecte do dolenibh exer iusto elis nit nulland reetum eros nullaore minim veliquat, quat lorpercing euisl er amet autat prat iustisi tat nos nim dolortie magna faccummodip et luptat. Ipit volorem quat luptatuer sectem augait nisim zzrilis nim et venisim iriusci et wisit lutatinibh euipsusci blam, consequipis nostinim nonsenim aliquis sequis doloreet, quat. Mod eleniam cortin hendit, velent irit ut augueriuscil ipit venit la facillandre mod magnibh ex ero odipsum dolent dolor sequisim nullam, quismol ortismodigna feu faccum ing et, quam, voloreet illam vel elessequisi.</p>
        <p>Volestincin henis at etuer susto cortie magna adit arcil et lum ipiscilisis nulla feuis nosto erit nosto consenismet veliquis nis nibh essi.</p>
        <p>Os elenim il utpat alit non ulputate min hent autet wisi ea con ulput wis euipsustio consectem vulla faccum quis dolore feu faccumsan utatisis nos adignibh euisim ip et at, ver sum dipsuscil utem vullaor erosto odigna ad tat. Dolestrud enim nonum dolor inlit exerit dignim il eliquisi bla commy num quatum vel er ate erat. Ipsuscilla feu facidunt wissed mincili quisit nit venis augait dolor accum et, quip essi.</p>
        <p>Ud tisi. Lore do consed essim irit adigniam, conullu ptatum ipit vel ut nonse consed eugiam vel exerost ionulputat am, conse eum vel ipis niam veniscidui tationum nummy nisim nosto exerosto con ullupat accum ad eum ipit, cor susci tio odiam diat adam dolorem iustrud do eu feu feugiat voloborem et, quis nonsenit euipit wis nisl el init wisi.</p>
      </div>
      <div class="company-mark"><span class="company-mark__square"></span><span>Ridgeline Bank</span></div>
    </article>

  </section>

</body>
</html>
```